Laundry pickup and delivery flyer "Fold Harbor laundry"

I need a flyer "8.5"x11" that tells customers about our pickup and delivery laundry service. our website address is: www.foldharborlaundry.example The flyer should be front and back.

Font styles to use
Sans Serif

Colors
0094D4
00A9DD
6FCCEA
C7EBF8
E9F6FB

```html
<!DOCTYPE html>
<html lang="en">
<head>
<meta charset="utf-8">
<title>Fold Harbor laundry – Pickup &amp; Delivery Flyer</title>
<link rel="stylesheet" href="https://fonts.googleapis.com/css2?family=Saira+Condensed:ital,wght@0,700;0,800;1,700;1,800&family=Mulish:wght@400;600;700&display=swap">
<style>
  :root{
    --brand-deep:#1a3fae;
    --brand:#0094d4;
    --brand-bright:#00a9dd;
    --brand-sky:#6fccea;
    --brand-mist:#c7ebf8;
    --brand-ice:#e9f6fb;
    --ink:#3a4250;
    --paper:#ffffff;
    --backdrop:#a9b0b8;
  }
  *{box-sizing:border-box;margin:0;padding:0}
  html,body{width:1200px;height:1200px;overflow:hidden;background:var(--backdrop)}
  .stage{position:relative;width:1200px;height:1200px}
  .page{position:absolute;top:272px;width:504px;height:648px;background:var(--paper);overflow:hidden;box-shadow:0 2px 8px rgba(0,0,0,.25);font-family:"Mulish",sans-serif;color:var(--ink)}
  .page--front{left:68px}
  .page--back{left:617px}
  .abs{position:absolute}
  .heading{font-family:"Saira Condensed",sans-serif;font-style:italic;font-weight:800;text-transform:uppercase;line-height:1}
  .wordmark{font-family:"Saira Condensed",sans-serif;font-weight:800;color:var(--brand);display:flex;align-items:center;gap:8px;font-size:27px;line-height:1;text-transform:uppercase}
  .wordmark__dot{width:16px;height:16px;border-radius:50%;background:var(--brand-bright)}
  .wordmark small{display:block;font-size:11px;letter-spacing:2px;font-weight:800}
  .photo{position:absolute}
  .body-copy{font-size:7.2px;line-height:1.5;color:var(--ink)}

  /* front */
  .hero-banner{left:0;top:240px;width:224px;height:108px;color:#fff;padding:10px 0 0 22px;z-index:2}
  .hero-banner h1{font-size:34px;white-space:nowrap}
  .hero-banner h2{font-size:19px;line-height:1.08;white-space:nowrap}
  .tagline-bar{left:10px;top:396px;width:262px;height:19px;background:var(--brand-deep);color:#fff;font-size:14px;padding:2px 0 0 22px}
  .pickup-box{left:314px;top:362px;width:110px;height:54px;background:var(--brand-deep);color:#fff;font-size:19px;text-align:center;padding-top:6px;transform:skewX(-8deg)}
  .intro{left:14px;top:422px;width:476px}
  .how-panel{left:0;top:476px;width:504px;height:124px}
  .how-title{left:150px;top:466px;width:170px;height:24px;background:var(--brand);color:#fff;font-size:18px;text-align:center;padding-top:3px;transform:skewX(-12deg)}
  .steps{left:4px;top:492px;width:496px;height:104px;display:grid;grid-template-columns:repeat(4,1fr);gap:4px}
  .step{display:flex;flex-direction:column;align-items:center;text-align:center;color:#fff;font-size:7.2px;line-height:1.4;padding:14px 12px 0}
  .step svg{width:44px;height:44px;margin-bottom:8px}

  .footer{left:0;top:598px;width:504px;height:50px;background:#fff}
  .footer__phone{left:0;top:3px;width:292px;height:44px;background:var(--brand-bright);border-radius:0 24px 24px 0;color:#fff;font-size:21px;padding:11px 0 0 166px;white-space:nowrap}
  .footer__call{left:0;top:3px;width:150px;height:44px;background:var(--paper);border-radius:0 24px 24px 0;font-size:20px;color:var(--brand-deep);padding:12px 0 0 20px;white-space:nowrap;z-index:2}
  .footer__web{right:24px;top:18px;font-size:11.5px;color:var(--ink)}

  /* back */
  .why{left:30px;top:324px;color:#fff}
  .why h2{font-size:28px;margin-bottom:12px;white-space:nowrap}
  .checklist{list-style:none;width:190px}
  .checklist li{display:flex;gap:8px;font-size:7.6px;line-height:1.45;margin-bottom:9px}
  .checklist svg{flex:none;width:10px;height:10px;margin-top:1px}
  .section-bar{height:22px;background:var(--brand);color:#fff;font-size:15px;padding:3px 0 0 14px;white-space:nowrap}
  .section-bar--res{left:248px;top:324px;width:236px}
  .section-bar--com{left:248px;top:444px;width:236px}
  .res-copy{left:258px;top:352px;width:226px}
  .com-copy{left:258px;top:474px;width:226px}
  .pricing{left:28px;top:494px;width:200px;height:86px;background:var(--brand-bright);border:2px solid #fff;border-radius:8px}
  .pricing__title{left:10px;top:7px;color:#fff;font-size:21px;white-space:nowrap}
  .pricing__inner{left:6px;top:34px;width:186px;height:44px;background:#fff}
  .pricing__label{left:4px;top:3px;width:36px;height:38px;background:var(--brand-deep);color:#fff;font-size:10px;text-align:center;padding-top:3px;font-style:normal}
  .pricing__amount{left:50px;top:-1px;color:var(--brand-deep);font-size:46px}
  .pricing__unit{left:152px;top:26px;color:var(--brand-deep);font-size:8px}
</style>
</head>
<body>
<main class="stage">

  <section class="page page--front">
    <div class="photo" role="img" aria-label="Photo of a row of stainless steel front-loading washers in a laundromat" style="left:0;top:44px;width:492px;height:214px;background:linear-gradient(180deg,#9a958f 0%,#c9ccd0 45%,#8c8f93 100%)"></div>

    <svg class="abs" style="left:0;top:0" width="504" height="480" viewBox="0 0 504 480" aria-hidden="true">
      <defs>
        <linearGradient id="fBlue" x1="0" x2="1"><stop offset="0" stop-color="#00a9dd"/><stop offset="1" stop-color="#1a3fae"/></linearGradient>
      </defs>
      <path d="M180 0 H504 V60 C430 30 330 60 250 55 C220 50 200 30 180 0Z" fill="#fff"/>
      <path d="M230 58 C330 60 420 20 504 12 V52 C430 48 340 80 230 58Z" fill="url(#fBlue)"/>
      <path d="M260 66 C360 78 440 50 504 56 V66 C440 64 360 92 260 66Z" fill="#c7ebf8"/>
      <path d="M0 44 H30 C20 60 10 64 0 66Z" fill="#fff"/>
      <path d="M0 228 C120 200 280 218 504 190 V390 H0Z" fill="#fff"/>
      <path d="M0 236 C140 210 300 222 504 198 V214 C300 238 140 226 0 252Z" fill="url(#fBlue)"/>
      <path d="M0 258 C90 236 200 238 300 240 L290 352 C200 360 90 350 0 362Z" fill="#00a9dd"/>
      <path d="M0 350 C160 328 340 350 504 320 V360 C340 386 160 360 0 380Z" fill="url(#fBlue)"/>
      <path d="M0 370 C160 352 340 372 504 346 V352 C340 380 160 360 0 378Z" fill="#6fccea"/>
      <path d="M0 386 C160 370 340 392 504 366 V420 H0Z" fill="#fff"/>
      <polygon points="284,390 292,390 286,416 278,416" fill="#6fccea"/>
      <polygon points="298,390 308,390 302,416 292,416" fill="#00a9dd"/>
    </svg>

    <div class="abs wordmark" style="left:22px;top:26px"><span class="wordmark__dot"></span><span>Fold Harbor<small>Laundry and Dry Cleaning</small></span></div>

    <div class="photo" role="img" aria-label="Photo of the branded white and blue delivery van" style="left:226px;top:266px;width:268px;height:96px;border-radius:14px 30px 10px 10px;background:linear-gradient(90deg,#1a55c4 0%,#eef4f8 45%,#ffffff 70%,#2a4fb8 100%)"></div>

    <div class="abs hero-banner heading">
      <h1>Fold Harbor</h1>
      <h2>Harborview's Premier<br>Laundry Service</h2>
    </div>

    <div class="abs tagline-bar heading">Clean Clothes in a Few Clicks</div>
    <div class="abs pickup-box heading">Pick Up &amp;<br>Delivery</div>

    <p class="abs intro body-copy">Fold Harbor - Harborview, Maine's most advanced and professional laundry service - takes the work out of laundry day with our instant pickup and delivery system. With just a few clicks you can sign up for service and schedule a pickup and delivery time that fits your busy schedule. Your clothes are expertly cleaned to your specifications, folded, packaged, and delivered back to you for easy storage.</p>

    <svg class="abs how-panel" viewBox="0 0 504 124" aria-hidden="true">
      <rect width="504" height="124" fill="#00a9dd"/>
      <rect x="4" y="16" width="120" height="104" rx="10" fill="#0094d4"/>
      <rect x="128" y="16" width="120" height="104" rx="10" fill="#1a6fd0"/>
      <rect x="252" y="16" width="120" height="104" rx="10" fill="#0094d4"/>
      <rect x="376" y="16" width="124" height="104" rx="10" fill="#1a3fae"/>
    </svg>
    <div class="abs how-title heading">How It Works</div>

    <div class="abs steps">
      <div class="step">
        <svg viewBox="0 0 44 44"><circle cx="22" cy="22" r="20" fill="none" stroke="#fff" stroke-width="1.5"/><circle cx="22" cy="22" r="12" fill="none" stroke="#fff" stroke-width="2"/><path d="M22 14v8l5 4" stroke="#fff" stroke-width="2" fill="none" stroke-linecap="round"/></svg>
        Schedule a pickup here - feel free to leave your bag where our driver can get to it.
      </div>
      <div class="step">
        <svg viewBox="0 0 44 44"><circle cx="22" cy="22" r="20" fill="none" stroke="#fff" stroke-width="1.5"/><path d="M10 27V17h17l5 5v5z" fill="none" stroke="#fff" stroke-width="2" stroke-linejoin="round"/><circle cx="15" cy="28" r="2.5" fill="#fff"/><circle cx="28" cy="28" r="2.5" fill="#fff"/></svg>
        Our driver will pickup your clothes at the scheduled time.
      </div>
      <div class="step">
        <svg viewBox="0 0 44 44"><circle cx="22" cy="22" r="20" fill="none" stroke="#fff" stroke-width="1.5"/><rect x="13" y="11" width="18" height="22" rx="2" fill="none" stroke="#fff" stroke-width="2"/><circle cx="22" cy="24" r="5" fill="none" stroke="#fff" stroke-width="2"/><path d="M15 15h5" stroke="#fff" stroke-width="2"/></svg>
        Your clothes are expertly cleaned by our team of laundry professionals
      </div>
      <div class="step">
        <svg viewBox="0 0 44 44"><circle cx="22" cy="22" r="20" fill="none" stroke="#fff" stroke-width="1.5"/><path d="M22 17a3 3 0 1 0-3-3M22 17v2L10 28h24L22 19" fill="none" stroke="#fff" stroke-width="2" stroke-linejoin="round" stroke-linecap="round"/></svg>
        We delivery your clean clothes back to you at your convenience!
      </div>
    </div>

    <footer class="abs footer">
      <div class="abs footer__phone heading">555-014-2290</div>
      <div class="abs footer__call heading">Call Us Now</div>
      <div class="abs footer__web">www.foldharborlaundry.example</div>
    </footer>
  </section>

  <section class="page page--back">
    <div class="photo" role="img" aria-label="Photo of hands holding a stack of folded knit sweaters" style="left:0;top:0;width:330px;height:300px;background:linear-gradient(135deg,#d8cfc8 0%,#b89a90 35%,#5c6470 70%,#2a2e36 100%)"></div>

    <svg class="abs" style="left:0;top:0" width="504" height="648" viewBox="0 0 504 648" aria-hidden="true">
      <defs>
        <linearGradient id="bBlue" x1="0" x2="1"><stop offset="0" stop-color="#00a9dd"/><stop offset="1" stop-color="#1a3fae"/></linearGradient>
        <linearGradient id="bPanel" x1="0" y1="0" x2="0" y2="1"><stop offset="0" stop-color="#0094d4"/><stop offset="1" stop-color="#00a9dd"/></linearGradient>
      </defs>
      <path d="M230 0 H504 V110 C430 110 350 60 300 0Z" fill="#fff"/>
      <path d="M250 0 C300 60 360 100 440 110 C470 112 490 106 504 100 V114 C480 124 440 124 400 116 C330 100 280 50 230 0Z" fill="url(#bBlue)"/>
      <path d="M330 110 C400 130 460 126 504 114 V270 C420 250 360 240 330 260Z" fill="#1f2630"/>
      <path d="M330 150 C400 180 460 176 504 160 V180 C460 196 400 200 330 176Z" fill="#fff"/>
      <path d="M0 300 C120 280 250 280 504 190 V300 H0Z" fill="#1a3fae"/>
      <path d="M0 286 C140 268 260 262 504 172 V206 C300 280 140 290 0 310Z" fill="url(#bBlue)"/>
      <path d="M0 300 C150 286 300 300 504 230 V300 H0Z" fill="#fff"/>
      <path d="M0 296 H247 V598 H0Z" fill="url(#bPanel)"/>
      <path d="M0 300 C80 290 170 292 247 298 V308 H0Z" fill="#1a3fae"/>
      <polygon points="488,324 494,324 490,346 484,346" fill="#fff"/>
    </svg>

    <div class="abs wordmark" style="left:326px;top:22px;font-size:24px"><span class="wordmark__dot"></span><span>Fold Harbor<small style="font-size:10px">Laundry and Dry Cleaning</small></span></div>

    <div class="photo" role="img" aria-label="Photo of the branded white and blue delivery van" style="left:224px;top:206px;width:262px;height:96px;border-radius:14px 30px 10px 10px;background:linear-gradient(90deg,#1a55c4 0%,#eef4f8 45%,#ffffff 70%,#2a4fb8 100%)"></div>

    <div class="abs why">
      <h2 class="heading">Why Fold Harbor?</h2>
      <ul class="checklist">
        <li><svg viewBox="0 0 10 10"><circle cx="5" cy="5" r="5" fill="#fff"/><path d="M2.5 5l1.8 1.8L7.6 3.4" stroke="#0094d4" stroke-width="1.4" fill="none"/></svg>Our laundry professionals separate lights and darks to keep your clothes looking great!</li>
        <li><svg viewBox="0 0 10 10"><circle cx="5" cy="5" r="5" fill="#fff"/><path d="M2.5 5l1.8 1.8L7.6 3.4" stroke="#0094d4" stroke-width="1.4" fill="none"/></svg>Your items will never be washed with anyone else's</li>
        <li><svg viewBox="0 0 10 10"><circle cx="5" cy="5" r="5" fill="#fff"/><path d="M2.5 5l1.8 1.8L7.6 3.4" stroke="#0094d4" stroke-width="1.4" fill="none"/></svg>We use high quality detergents and eco friends chemicals</li>
        <li><svg viewBox="0 0 10 10"><circle cx="5" cy="5" r="5" fill="#fff"/><path d="M2.5 5l1.8 1.8L7.6 3.4" stroke="#0094d4" stroke-width="1.4" fill="none"/></svg>No more Laundry day!</li>
      </ul>
    </div>

    <div class="abs section-bar section-bar--res heading">Residential Delivery Service</div>
    <p class="abs res-copy body-copy">Utilize our laundry pickup and delivery service to make laundry day easy. Don't waste your free time doing laundry. Go and do life instead. We pick up your laundry at your doorstep and return it the next day to the same spot. Your professionally cleaned and folded clothes will be delivered back to you ready for the drawer or closet!</p>

    <div class="abs section-bar section-bar--com heading">Commercial Laundry Service</div>
    <p class="abs com-copy body-copy">Let us help your business grow by taking the burden of laundry off of you. Our commercial grade washing, highly seasoned process and quality assurances will ensure your business thrives. So invest in your business and send those dirty towels, aprons, bedding or any other washable items that your business needs to be spotless. Gain ROI instantly by selecting Fold Harbor as your cleaning partner against dirt and stains. Focus your time on your business instead!</p>

    <div class="abs pricing">
      <div class="abs pricing__title heading">Pricing &amp; Services</div>
      <div class="abs pricing__inner">
        <div class="abs pricing__label heading">Wash<br>and<br>Fold</div>
        <div class="abs pricing__amount heading">$1.50</div>
        <div class="abs pricing__unit heading">/Pound</div>
      </div>
    </div>

    <footer class="abs footer">
      <div class="abs footer__phone heading">555-014-2290</div>
      <div class="abs footer__call heading">Call Us Now</div>
      <div class="abs footer__web">www.foldharborlaundry.example</div>
    </footer>
  </section>

</main>
</body>
</html>
```